Games for Classrooms Website Redesign

The purpose of the website redesign is to freshen up the content and update it to give a more modern look and feel. It will show what we do concisely and satisfy all potential visitors. We work with primary schools and the brand is fun.About: Games for Classrooms is a scheme that brings top Zentara athletes into primary schools to inspire children to do more physical activity. We typically run a half day event at the school where the athlete does a fun fitness circuit with the children and then an inspirational assembly with a demonstration and Q&A. The children are asked to collect sponsorship money to take part in the event and a large proportion of the money raised goes back to the school in the form of a voucher for them to spend on new sports equipment. 1. To generate more leads from potential customers/schools2. To engage the children and parents more in the event and get them excited for their upcoming visit whilst setting up a fundraiser page.3. To simplify and modernise what is already there.

I have attached some ideas for each of the pages (uploaded in brief)

Here is a link to our current website: www.gamesforclassrooms.example

I have also attached a link to the sponsorship form which shows the kind of look and feel we're after.

Target Market(s)

Primary school teachers
Primary school parents

Number of Pages Required

5+ page

Requirements
Must have
• Fun, modern.
• Be built on plover scaffold

```html
<!DOCTYPE html>
<html lang="en">
<head>
<meta charset="utf-8">
<title>Games for Classrooms</title>
<link rel="stylesheet" href="https://fonts.googleapis.com/css2?family=Montserrat:wght@500;600;700;800&display=swap">
<style>
:root{
  --ink:#111111;
  --white:#ffffff;
  --red:#e8182f;
  --blue:#17a3fb;
  --green:#2ec10a;
  --orange:#ff3d22;
  --footer:#1e1e1e;
  --footer-text:#e6e6e6;
  --footer-green:#35b81c;
}
*{box-sizing:border-box;margin:0;padding:0}
html,body{width:729px;height:1200px;overflow:hidden;background:var(--white)}
body{font-family:'Montserrat',Arial,sans-serif;color:var(--ink)}
.page{position:relative;width:729px;height:1200px;overflow:hidden}

.site-header{position:absolute;top:0;left:0;width:729px;height:57px;border-bottom:1px solid #eeeeee;display:flex;align-items:center;justify-content:space-between;padding:0 33px 0 40px}
.brand{display:flex;align-items:center;gap:5px;font-weight:700;font-size:7px;letter-spacing:.2px;color:var(--red)}
.brand-dot{width:14px;height:14px;border-radius:50%;background:var(--red)}
.menu-toggle{display:flex;align-items:center;gap:7px;font-weight:700;font-size:7.5px;letter-spacing:.8px}
.menu-lines{display:flex;flex-direction:column;gap:3px}
.menu-lines span{display:block;width:22px;height:2px}

.mission{position:absolute;top:58px;left:0;width:729px;height:187px}
.mission-text{position:absolute;left:40px;right:0;top:56px;text-align:center;font-weight:700;font-size:14px;line-height:15.6px;letter-spacing:.9px;text-transform:uppercase}

.hero-photo{position:absolute;top:245px;left:0;width:729px;height:296px;background:linear-gradient(100deg,#7a4a34 0%,#c99a6e 25%,#e6c23a 45%,#b0785a 65%,#e9c94a 80%,#8a5a44 100%)}

.audience-link{position:absolute;top:592px;width:132px;height:132px;border-radius:50%;display:flex;align-items:center;justify-content:center;text-align:center;color:var(--white);font-weight:700;font-size:16px;line-height:19px;text-decoration:none}
.school{left:172px;background:var(--red)}
.parent{left:423px;background:var(--blue)}

.stats-title{position:absolute;top:798px;left:0;width:729px;text-align:center;font-weight:700;font-size:14px;letter-spacing:.3px}
.stat{position:absolute;top:846px;width:89px;height:52px;border-radius:5px;color:var(--white);text-align:center}
.stat-outline{position:absolute;top:851px;width:89px;height:52px;border:1.5px solid var(--ink);border-radius:5px;border-top-color:transparent;border-right-color:transparent}
.stat-label{display:block;font-weight:700;font-size:8px;padding-top:8px;line-height:9px}
.stat-value{display:block;font-weight:800;font-size:25px;line-height:25px}
.stat-clubs{left:172px;background:var(--green)}
.stat-clubs .stat-label{font-size:9.5px}
.stat-schools{left:328px;background:var(--blue)}
.stat-children{left:484px;background:var(--orange)}

.site-footer{position:absolute;top:978px;left:0;width:729px;height:222px;background:var(--footer);color:var(--footer-text);text-align:center;font-size:5.6px;letter-spacing:.4px;line-height:8.4px}
.footer-nav{position:absolute;top:20px;left:0;right:0;font-weight:500}
.footer-nav a{color:var(--footer-text);text-decoration:none;text-transform:uppercase}
.footer-brand{position:absolute;top:58px;left:0;right:0;display:flex;justify-content:center;align-items:center;gap:4px;font-weight:700;font-size:7px;color:var(--white)}
.footer-brand .brand-dot{width:12px;height:12px;background:var(--white)}
.footer-legal{position:absolute;top:87px;left:0;right:0}
.footer-contact{position:absolute;top:118px;left:0;right:0}
.footer-contact .label{color:var(--footer-green)}
.social{position:absolute;top:168px;left:0;right:0;display:flex;justify-content:center;gap:6px}
.social span{width:11px;height:11px;background:var(--footer-green);border-radius:1px}
.copyright{position:absolute;top:197px;left:0;right:0;text-transform:uppercase}
</style>
</head>
<body>
<div class="page">

  <header class="site-header">
    <div class="brand"><span class="brand-dot"></span>GAMES FOR CLASSROOMS</div>
    <div class="menu-toggle">
      <div class="menu-lines"><span style="background:var(--red)"></span><span style="background:var(--blue)"></span><span style="background:var(--green)"></span></div>
      MENU
    </div>
  </header>

  <section class="mission">
    <p class="mission-text">Our mission is to put physical<br>health in children on a par with<br>mental health and academic<br>excellence.</p>
  </section>

  <div class="hero-photo" role="img" aria-label="Photo of smiling primary school children in bright t-shirts taking part in an activity in a school hall"></div>

  <a class="audience-link school" href="#">I’M A<br>SCHOOL</a>
  <a class="audience-link parent" href="#">I’M A<br>PARENT</a>

  <h2 class="stats-title">OUR STATS</h2>
  <span class="stat-outline" style="left:166px"></span>
  <div class="stat stat-clubs"><span class="stat-label">CLUBS RUNS</span><span class="stat-value">3003</span></div>
  <span class="stat-outline" style="left:322px"></span>
  <div class="stat stat-schools"><span class="stat-label">SCHOOLS HELPED</span><span class="stat-value">279</span></div>
  <span class="stat-outline" style="left:478px"></span>
  <div class="stat stat-children"><span class="stat-label">CHILDREN INSPIRED</span><span class="stat-value">38321</span></div>

  <footer class="site-footer">
    <nav class="footer-nav"><a href="#">Sitemap</a> | <a href="#">Cookies</a> | <a href="#">Privacy Policy</a> | <a href="#">Online Fundraising</a></nav>
    <div class="footer-brand"><span class="brand-dot"></span>GAMES FOR CLASSROOMS</div>
    <p class="footer-legal">Games for Classrooms and GFC Coaching are trading names of the Social Enterprise<br>called Playwell Ventures Limited, a company registered in England no. 01234567.</p>
    <p class="footer-contact">
      <span class="label">Telephone:</span> 01632 960100 (GB) or 01 555 0142 (Ireland)<br>
      <span class="label">Email:</span> hello@gamesforclassrooms.example<br>
      <span class="label">Snailmail (we love a letter!):</span><br>
      GAMES for CLASSROOMS 12 Orchard Yard, Meadow Business Park, Northfield NF1 2AB<br>
      GAMES for CLASSROOMS Harbour House, Quay Lane, Seaport 4 Ireland
    </p>
    <div class="social" aria-label="Social links"><span></span><span></span><span></span></div>
    <p class="copyright">© 2019 Games for Classrooms</p>
  </footer>

</div>
</body>
</html>
```